Website to promote New Zealand as a destination by BKR

We are a company that promotes New Zealand education, migration, business and travel opportunities. We want a website to reflect all these activities. We have an existing website that should be used as a base template and add the other required pages to it. The current website is what we want to expand upon. Access to the files of the current website may not be possible since the previous designer cannot be contacted. So the new designer has to use the existing template and build the whole thing from there. It should be an easy job since there is already a clear sample of what we want. I would like the same flow to continue where the impact is very high visually and very little text content. I expect most clients to use a mobile device to access the site. so it has to be extremely mobile friendly.
Updates

Target Market(s)

Anybody between ages of 16-60 who would like to study, settle, work, travel or invest in New Zealand.

Industry/Entity Type

Education

Contact Information for Business Card

Devan Mirza
Licensed Immigration Adviser
License No 308741925

Mob: +64 219837462
Email: devan.mirza@bkrgroup.example
BKR Services Limited
417 Tanner Lane
Ashbury
Hamilton
New Zealand - 3210

www.bkrgroup.example

Coding

Coded - Design and coding required

Number of Pages Required

5+ page

Font styles to use
Sans Serif

Requirements
Must have
• MUST use the existing design of our website and build other pages from it.
Should not have
• Nil

```html
<!DOCTYPE html>
<html lang="en">
<head>
<meta charset="utf-8">
<title>BKR – Think New Zealand</title>
<link href="https://fonts.googleapis.com/css2?family=Open+Sans:ital,wght@0,300;0,400;0,600;0,700;0,800;1,800&display=swap" rel="stylesheet">
<style>
:root{
  --canvas:#ffffff;
  --nav:#3b3b3b;
  --ink:#444444;
  --panel:#1f1f1f;
  --black:#050505;
  --purple:#6b1c6e;
  --purple-line:#9a4a9c;
  --pink:#e8336d;
  --white:#ffffff;
  --muted:#bbbbbb;
  --footer:#454545;
}
*{box-sizing:border-box;margin:0;padding:0}
html,body{width:1200px;height:1120px;overflow:hidden;background:var(--canvas)}
body{font-family:"Open Sans",sans-serif;color:var(--ink);position:relative}
.page{position:absolute;left:464px;top:0;width:273px;height:1120px;overflow:hidden;background:var(--white)}
.abs{position:absolute}
.center{left:0;right:0;text-align:center}

/* header + hero */
.hero{top:0;left:0;width:273px;height:165px;background:radial-gradient(ellipse at 75% 30%,#5a5356 0%,#2a2829 40%,#0d0d0d 80%)}
.nav{top:0;left:0;width:273px;height:24px;background:var(--nav);opacity:.95}
.brand{left:22px;top:6px;display:flex;align-items:center;gap:3px;color:var(--white);font-weight:600;font-size:9px;letter-spacing:.5px}
.brand-dot{width:11px;height:11px;border-radius:50%;border:1px solid var(--white)}
.menu{left:66px;top:11px;display:flex;gap:4px;font-size:2.6px;color:#dddddd;letter-spacing:.1px}
.hero-title{left:22px;top:56px;font-size:11.5px;font-weight:300;color:var(--white)}
.hero-sub{left:22px;top:75px;font-size:6.3px;font-weight:300;color:var(--white);line-height:8px}
.btn-solid{height:11px;width:47px;background:var(--purple);color:var(--white);font-size:3.4px;display:flex;align-items:center;justify-content:center;top:127px}

/* overview */
.h2{font-size:11.5px;font-weight:300;color:#3a3a3a;letter-spacing:.2px}
.overview-title{top:178px}
.overview-copy{left:38px;width:197px;top:198px;font-size:2.7px;line-height:5.2px;text-align:center;color:#777}
.icon{top:230px;width:24px;height:24px}
.btn-outline{top:260px;height:11px;width:47px;border:.8px solid var(--purple-line);border-radius:2px;color:var(--purple);font-size:3.1px;display:flex;align-items:center;justify-content:center;background:var(--white)}

/* proverb */
.proverb{top:286px;left:0;width:273px;height:140px;background:linear-gradient(90deg,#5a2a0c,#9a5a1c 25%,#b06a22 50%,#9a5a1c 75%,#5a2a0c)}
.proverb-box{left:92px;top:24px;width:89px;height:90px;border-radius:14px;border:1.5px solid rgba(60,25,5,.7);background:linear-gradient(180deg,rgba(255,235,200,.45),rgba(150,80,25,.35) 35%,rgba(120,60,20,.25));text-align:center;color:var(--white);padding-top:36px}
.proverb-maori{font-size:4.8px;font-weight:800;font-style:italic;line-height:5.5px}
.proverb-en{font-size:4.8px;font-weight:800;line-height:5.5px;margin-top:3px}
.proverb-src{font-size:3.2px;margin-top:2px}

/* my new zealand */
.mnz-title{top:434px}
.row{left:0;width:273px;height:65px}
.photo{position:absolute;top:0;height:100%}
.label{position:absolute;top:0;height:100%;background:var(--panel);color:var(--white);font-size:11.5px;font-weight:300;display:flex;align-items:center;justify-content:center;letter-spacing:.3px}
.city{background:linear-gradient(180deg,#a07ab8,#6b4a86 60%,#7a5a8e)}
.fern{background:linear-gradient(90deg,#2f5a16,#5f8a2e 40%,#3c4a30 70%,#6a8a3a)}
.beach{background:linear-gradient(180deg,#6aa6c4 0%,#3f8a96 45%,#b9a27e 75%,#4a4a3a)}
.river{background:linear-gradient(160deg,#3a6a1c,#5a8e2a 40%,#4a9ab8 70%,#2e7ea8)}
.caption{left:8px;top:31px;font-size:3px;font-weight:600;color:var(--white)}

/* board */
.board{top:725px;left:0;width:273px;height:139px;background:linear-gradient(120deg,#000 55%,#1a1a1a 75%,#0a0a0a)}
.board-title{top:14px;color:var(--white)}
.member{top:37px;width:50px}
.portrait{width:49px;height:47px;background:linear-gradient(180deg,#c9ccd2,#8a8c92)}
.member-name{font-size:3.3px;font-weight:700;color:var(--white);margin-top:4px}
.member-bio{font-size:2.6px;line-height:5.3px;color:var(--muted);margin-top:3px}

/* blogs */
.blogs{top:866px;left:0;width:273px;height:136px;background:radial-gradient(ellipse at 50% 70%,#8a7a78 0%,#4a2a30 45%,#1e0f1a 85%)}
.blogs-title{top:15px;color:var(--white)}
.card{top:42px;width:67px;height:58px;background:var(--white);border:1.5px solid #e9e9e9;padding:5px 8px;box-shadow:0 1px 3px rgba(0,0,0,.4)}
.card-title{font-size:3.1px;line-height:4px;color:#333}
.card-meta{font-size:2.3px;color:#888;margin-top:3px}
.card-text{font-size:2.5px;line-height:4.4px;color:#666;margin-top:5px}
.btn-pink{height:9px;width:40px;border-radius:3px;background:var(--pink);color:var(--white);font-size:3px;display:flex;align-items:center;justify-content:center}

/* contact */
.contact{top:1005px;left:0;width:273px;height:103px;background:radial-gradient(ellipse at 70% 40%,#7a2a8e 0%,#4a1a5e 45%,#2a0a2e 80%)}
.contact-title{top:14px;color:var(--white)}
.field{left:30px;width:80px;height:8px;background:rgba(40,20,90,.75);font-size:2.5px;color:#aaa;padding:2.5px 4px}
.textarea{left:115px;top:39px;width:79px;height:37px;background:rgba(40,20,90,.75);font-size:2.5px;color:#aaa;padding:2.5px 4px}
.addr{left:203px;top:39px;color:var(--white)}
.addr-name{font-size:4.6px;font-weight:700}
.addr-lines{font-size:2.4px;line-height:4.2px}
.socials{display:flex;gap:1.5px;margin-top:2px}
.socials span{width:5px;height:5px;border-radius:50%;border:.6px solid var(--white)}
.footer{top:1108px;left:0;width:273px;height:12px;background:var(--footer);color:#ddd;font-size:2.6px;display:flex;align-items:center;justify-content:center}
</style>
</head>
<body>
<div class="page">

  <header class="abs hero" role="img" aria-label="Dark faceted geometric blocks background"></header>
  <nav class="abs nav">
    <div class="abs brand"><span class="brand-dot"></span>BKR</div>
    <div class="abs menu"><span>HOME ▾</span><span>EDUCATION</span><span>MIGRATION</span><span>WORK</span><span>BUSINESS</span><span>TRAVEL</span><span>MIGRATION SERVICES ▾</span><span>INFOTECH SERVICES ▾</span><span>CONTACT</span></div>
  </nav>
  <h1 class="abs hero-title">THINK NEW ZEALAND.</h1>
  <p class="abs hero-sub">ONE AMAZING COUNTRY,<br>MANY AWESOME OPPORTUNITIES.</p>
  <a class="abs btn-solid" style="left:37px">OVERVIEW</a>
  <a class="abs btn-solid" style="left:113px">MY NEW ZEALAND</a>
  <a class="abs btn-solid" style="left:188px">BLOGS</a>

  <section>
    <h2 class="abs center h2 overview-title">OVERVIEW</h2>
    <p class="abs overview-copy">BKR is a passionate and professional promoter of New Zealand education, migration, work, business and travel opportunities. Success through simplicity is the credo that underpins all our products and services for the benefit of our customers, employees, shareholders and community. New Zealand is more than breathtaking places and friendly people. In a world that struggles with myriad issues, the heart of the Pacific is a tranquil zone of safety, security and opportunity. Haere mai. Welcome to Aotearoa.</p>
    <svg class="abs icon" style="left:66px" viewBox="0 0 24 24" fill="none" stroke="#8a2a8e" stroke-width="1" stroke-linejoin="round"><path d="M2 12 L22 3 L15 21 L11 14 Z"/><path d="M11 14 L22 3"/><path d="M11 14 L10 20 L13 16"/></svg>
    <svg class="abs icon" style="left:182px" viewBox="0 0 24 24" fill="none" stroke="#8a2a8e" stroke-width="1" stroke-linecap="round"><circle cx="11" cy="7" r="5"/><path d="M9 7 V17 L7 15 Q5 15 6 17 L9 22 H17 L18 15 Q18 12 15 12 L11 11 V7 Q11 6 10 6 Q9 6 9 7"/></svg>
    <a class="abs btn-outline" style="left:54px">Migration Services</a>
    <a class="abs btn-outline" style="left:170px">Infotech Services</a>
  </section>

  <section class="abs proverb" role="img" aria-label="Warm wooden plank wall background">
    <div class="abs proverb-box">
      <p class="proverb-maori">HE TAONGA RONGONUI TE<br>AROHA KI TE TANGATA</p>
      <p class="proverb-en">GOODWILL TOWARDS<br>OTHERS IS A<br>PRECIOUS TREASURE</p>
      <p class="proverb-src">Maori whakatauki (Proverb)</p>
    </div>
  </section>

  <section>
    <h2 class="abs center h2 mnz-title">MY NEW ZEALAND</h2>
    <div class="abs row" style="top:458px">
      <div class="photo city" style="left:0;width:165px" role="img" aria-label="City skyline with a tower, tinted purple"></div>
      <p class="abs caption">A thriving first world economy. New Zealand compares with any other developed nation.</p>
      <div class="label" style="left:165px;width:108px">MODERN</div>
    </div>
    <div class="abs row" style="top:524px;height:66px">
      <div class="label" style="left:0;width:110px">BEAUTIFUL</div>
      <div class="photo fern" style="left:110px;width:163px" role="img" aria-label="Fern forest with a mossy stream"></div>
    </div>
    <div class="abs row" style="top:591px;height:66px">
      <div class="photo beach" style="left:0;width:167px" role="img" aria-label="Coastal beach with a large rock"></div>
      <div class="label" style="left:167px;width:106px">PEACEFUL</div>
    </div>
    <div class="abs row" style="top:658px">
      <div class="label" style="left:0;width:110px">INVITING</div>
      <div class="photo river" style="left:110px;width:163px" role="img" aria-label="Blue river winding through green bush"></div>
    </div>
  </section>

  <section class="abs board">
    <h2 class="abs center h2 board-title">OUR BOARD</h2>
    <div class="abs member" style="left:22px">
      <div class="portrait" role="img" aria-label="Portrait of Devan Mirza"></div>
      <p class="member-name">Devan Mirza</p>
      <p class="member-bio">He is the director and licensed immigration adviser. He has 12 years of experience in the industry.</p>
    </div>
    <div class="abs member" style="left:82px">
      <div class="portrait" role="img" aria-label="Portrait of Clara Whitfield"></div>
      <p class="member-name">Clara Whitfield</p>
      <p class="member-bio">She is the adviser for strategy and key relationships. She has 30 years of experience in the New Zealand education industry in senior positions.</p>
    </div>
    <div class="abs member" style="left:142px">
      <div class="portrait" role="img" aria-label="Portrait of Meera Sandhu"></div>
      <p class="member-name">Meera Sandhu</p>
      <p class="member-bio">She is the adviser for strategy, finance and corporate compliance. She is a Chartered Accountant with 15 years of experience.</p>
    </div>
    <div class="abs member" style="left:202px">
      <div class="portrait" role="img" aria-label="Portrait of Dr Lukas Varga"></div>
      <p class="member-name">Dr Lukas Varga</p>
      <p class="member-bio">He is the adviser for new products development and growth into global markets. Currently based in the US, he has 30 years of experience in the New Zealand education industry in senior positions.</p>
    </div>
  </section>

  <section class="abs blogs" role="img" aria-label="Laptop and coffee cup on a wooden desk">
    <h2 class="abs center h2 blogs-title">BLOGS</h2>
    <article class="abs card" style="left:16px">
      <p class="card-title">How To Turn Into A Developer Where To Get Trendy Write My</p>
      <p class="card-meta">by admin | Aug 8, 2016 | Tips</p>
      <p class="card-text">Every pupil must know the way simple or not to start from scratch, what saves to anticipate from your employers.</p>
    </article>
    <article class="abs card" style="left:102px">
      <p class="card-title">Six Myths Concerning The Fundamentals Of Modern</p>
      <p class="card-meta">by admin | Aug 8, 2016 | Uncategorized</p>
      <p class="card-text">Six myths concerning the fundamentals of contemporary schooling and six fresh rules to replace them.</p>
    </article>
    <article class="abs card" style="left:187px">
      <p class="card-title">How To Create A Research Report</p>
      <p class="card-meta">by admin | Aug 1, 2016 | Uncategorized</p>
      <p class="card-text">Quoting just one work narrative, essay or report within a series or anthology? Don't depend on an automatic details from the.</p>
    </article>
    <a class="abs btn-pink" style="left:116px;top:113px">View All</a>
  </section>

  <section class="abs contact" role="img" aria-label="Purple geometric backdrop">
    <h2 class="abs center h2 contact-title">CONTACT US</h2>
    <div class="abs field" style="top:39px">NAME</div>
    <div class="abs field" style="top:53px">EMAIL</div>
    <div class="abs field" style="top:67px">PHONE</div>
    <div class="abs textarea">TEXT</div>
    <div class="abs addr">
      <p class="addr-name">BKR GROUP</p>
      <p class="addr-lines">417 TANNER LANE,<br>ASHBURY,<br>HAMILTON, WAIKATO,<br>NEW ZEALAND 3210<br>EMAIL: devan.mirza@bkrgroup.example</p>
      <div class="socials"><span></span><span></span><span></span><span></span></div>
    </div>
    <a class="abs btn-pink" style="left:115px;top:83px">ENQUIRE</a>
  </section>

  <footer class="abs footer">© 2016 BKR GROUP | PRIVACY POLICY | ALL RIGHTS RESERVED.</footer>
</div>
</body>
</html>
```